Brisko Web Design Project

My company is engaged in the provision of advertising service (mostly contextual advertising - like Pellix bidwords or Murelka vector) . The website must show the potential my customers that brisko company earnestly provide quality service, and design must be is in cheerful colors - also fashionable and brisko. very much needed positive illustrations showing what we are doing service in a positive and easy, based on trust and loyalty. Website should be similar to the clear and classic navigation, include links - home - about -services/portfolio -contacts. need to specify the hours of operation office and phone number + office address.

Target Market(s)

small/medium business

Industry/Entity Type

Advertising

Requirements
Must have
• it is important to understand that a lot depends on the quality of content - content design, it is worth special attention. and sure - the use of branded elements of the logo in the design of the site and details of the content. content should look modern, but it is understood and allowed a little classics. in general, I always like modern coupled with a combination of classic and fun and playful at the same time, serious intentions of consciousness.
Nice to have
• I'll add some links designs as an example that I like the web projects
http://www.norvatek.ru/context/
http://www.lupora.ru/services/kontekstnaja_reklama/
http://www.zekta.ru/context/
http://halmivex.ru/service/context/

So I need personal design, also nice and concise, with no extra bells and whistles. design must be based on the logo and colors of brisko combines a my logo. Font should be used is the same as in the logo. background should be white or light.
Should not have
• As usual - extraneous colors (not included in the logo as an attachment to the brief) fonts hard to read, there should be a lot of very dark tones and luscious colors with contrast. navigation and content must be easily understood by the user. I am sorry for my bad english, and I hope that u have an understanding of my description. if you want to clarify what else the details. before doing any work, please feel free to ask me to clarify.

```html
<!DOCTYPE html>
<html lang="en">
<head>
<meta charset="utf-8">
<title>Brisko – Contextual Advertising</title>
<link href="https://fonts.googleapis.com/css2?family=Cambo&family=PT+Sans:ital,wght@0,400;0,700;1,400;1,700&display=swap" rel="stylesheet">
<style>
:root{
  --orange:#e8761e;
  --orange-deep:#d9620f;
  --btn:#f0a640;
  --lime:#c0dc4a;
  --sky:#acdde7;
  --butter:#fde9a6;
  --mint:#6bc29a;
  --panel:#f2f2f2;
  --line:#d4d4d4;
  --ink:#333;
  --footer:#5b5b5b;
  --head:"Cambo", Georgia, serif;
  --body:"PT Sans", Arial, sans-serif;
}
*{box-sizing:border-box;margin:0;padding:0}
html,body{width:913px;height:1200px;overflow:hidden}
body{position:relative;background:#fff;font-family:var(--body);color:var(--ink)}
.abs{position:absolute}

/* header */
.site-header{left:0;top:0;width:913px;height:102px;background:linear-gradient(#fbfbfb,#eeeeee);border-bottom:1px solid #dcdcdc}
.brand{display:flex;align-items:center;gap:12px}
.brand-mark{width:40px;height:40px;background:var(--orange);border-radius:4px}
.brand-name{font-family:var(--head);font-size:42px;color:#4a3a34;line-height:1}
.site-header .brand{left:38px;top:31px}
.lang{right:34px;top:13px;font-size:10px;font-weight:700;color:#777}
.lang b{color:#333}.lang em{font-style:normal;color:var(--orange)}
.contact-line{font-size:12px;font-weight:700;color:#333}
.contact-line span{color:var(--orange)}
.toll{font-size:12px;font-weight:700;color:#333}
.phone{font-size:20px;color:var(--orange)}

/* nav */
.social{left:35px;top:117px;display:flex;gap:12px;font-size:11px;color:#777}
.main-nav{left:0;top:116px;width:913px;height:24px;font-family:var(--head);font-size:12.5px}
.main-nav a{position:absolute;top:0;line-height:23px;color:#333;text-decoration:none;white-space:nowrap}
.main-nav a.current{background:var(--lime);border-radius:6px;width:60px;text-align:center}

/* hero */
.hero{left:35px;top:152px;width:843px;height:246px;border:3px solid #d8d1bb;background:radial-gradient(circle at 25% 60%,#f29a45,var(--orange) 55%,var(--orange-deep))}
.hero h1{position:absolute;left:37px;top:22px;font-family:var(--head);font-weight:400;font-size:40px;line-height:42px;color:#fff;letter-spacing:2.6px}
.hero h1 .dark{color:#2e2e2e}
.hero p{position:absolute;left:37px;top:104px;width:370px;font-size:14.5px;line-height:19.5px;color:#fff}
.hero-arrows{position:absolute;left:37px;top:208px;display:flex;gap:6px}
.hero-arrows span{width:20px;height:20px;border-radius:50%;background:#fff;display:flex;align-items:center;justify-content:center}
.hero-screen{position:absolute;left:438px;top:26px;width:190px;height:156px;border-radius:4px;background:linear-gradient(#f4f4f4,#cfd3d8 80%,#9da2a8)}
.hero-plus{position:absolute;left:644px;top:84px}
.hero-keywords{position:absolute;left:689px;top:26px;width:120px;height:154px;border-radius:4px;background:linear-gradient(#e98a3c,#e37a2a)}
.demo-btn{position:absolute;left:474px;top:198px;width:120px;height:27px;background:#7fc8d9;border-radius:3px;color:#1f3a45;font-size:11px;font-weight:700;display:flex;align-items:center;justify-content:center}

/* content */
.card{border-radius:8px}
.card h2{font-family:var(--head);font-weight:400;font-size:19.5px;color:#333}
.card p{font-size:10px;line-height:14px;color:#444}
.btn{display:inline-flex;align-items:center;justify-content:center;width:84px;height:26px;border-radius:7px;background:var(--btn);color:#fff;font-size:9.5px;font-weight:700}
.intro{left:35px;top:424px;width:609px;height:168px;background:var(--sky);padding:12px 13px}
.intro p{margin-top:7px;font-size:9.4px;letter-spacing:-0.05px}
.intro .btn{position:absolute;left:12px;top:134px}
.how{left:35px;top:611px;width:609px;height:167px;background:linear-gradient(90deg,#ebe6da,#ddd7c7)}
.how h2{position:absolute;left:13px;top:12px}
.how p{position:absolute;left:13px;top:39px;width:255px;line-height:16px}
.how .btn{position:absolute;left:13px;top:128px}
.how-shot{position:absolute;left:271px;top:8px;width:327px;height:159px;background:linear-gradient(#d9d9d9 0 10px,#f7f7f7 10px);border:1px solid #bfbfbf}
.benefits{left:35px;top:796px;width:609px;height:168px;background:var(--butter);padding:11px 13px}
.benefits ul{list-style:none;margin-top:7px}
.benefit{display:flex;align-items:center;gap:12px;height:43px;border-bottom:1px solid #e5d08f;width:584px}
.benefit:last-child{border-bottom:none}
.benefit .num{flex:none;width:27px;height:27px;border-radius:50%;background:var(--orange-deep);color:#fff;font-family:var(--head);font-size:17px;display:flex;align-items:center;justify-content:center}
.benefit p{font-weight:700;font-size:9.5px;line-height:14px;color:#333}

/* sidebar */
.quick{left:668px;top:424px;width:211px;height:260px;background:var(--lime);padding:10px 14px}
.quick h3{font-family:var(--head);font-weight:400;font-size:15px;color:#333;margin-bottom:6px}
.field{height:25px;background:#fff;border:1px solid #7fb3a0;border-radius:2px;margin-bottom:5px;font-size:10px;color:#999;padding:6px 9px}
.field.area{height:86px}
.submit{position:absolute;right:17px;bottom:12px;width:75px;height:24px;border-radius:4px;background:#f07f1e;color:#fff;font-size:10px;font-weight:700;display:flex;align-items:center;justify-content:center}
.side-panel{background:var(--panel);border:1px solid var(--line);border-radius:6px}
.certified{left:668px;top:698px;width:211px;height:130px;padding:9px 10px}
.certified h3,.clients h3{font-family:var(--head);font-weight:400;font-size:15px;line-height:20px;color:#333}
.certified p{font-size:9.5px;line-height:14px;color:#555;margin-top:8px;width:106px}
.certified p.wide{width:auto;margin-top:0}
.badge{position:absolute;left:124px;top:9px;width:76px;height:76px;border-radius:6px;background:#f3b531}
.clients{left:668px;top:835px;width:211px;height:130px;padding:7px 8px}
.client-grid{display:grid;grid-template-columns:92px 92px;gap:8px;margin-top:6px}
.client{height:40px;display:flex;align-items:center;justify-content:center;gap:6px;font-weight:700;font-size:12px;color:#333;background:#fff;border:1px solid #e0e0e0}
.client i{width:10px;height:10px;background:var(--orange);display:block}
.client.yellow{background:#f6e600;border-color:#f6e600}

/* bottom */
.mint{background:var(--mint);border-radius:4px;padding:10px 13px;color:#fff}
.mint h2{font-family:var(--head);font-weight:400;font-size:19.5px;color:#2d3a33}
.mint p{font-style:italic;font-size:10px;line-height:14px;margin-top:7px}
.reviews{left:35px;top:977px;width:414px;height:134px}
.quote-mark{position:absolute;font-family:var(--head);font-size:58px;color:#3f8b66;line-height:1}
.reviewer{text-align:right;margin-top:6px;font-style:italic;font-weight:700;font-size:10px;line-height:14px;margin-right:45px}
.reviewer b{color:#1f3a2b}.reviewer span{color:#f7f08a}
.news{left:464px;top:977px;width:415px;height:134px}
.news .date{font-size:11px;font-weight:700;color:#fde9a6;margin-top:6px}
.news p{margin-top:2px}
.more{position:absolute;right:12px;bottom:12px;font-size:10px;font-style:italic;font-weight:700;color:#2d3a33}

.site-footer{left:0;top:1122px;width:913px;height:78px;background:var(--footer);color:#fff}
.site-footer .brand{left:38px;top:14px;gap:8px}
.site-footer .brand-mark{width:22px;height:22px}
.site-footer .brand-name{font-size:24px;color:#fff}
.copy{left:35px;top:52px;font-family:var(--head);font-size:9px;color:#e0e0e0}
.site-footer .contact-line,.site-footer .toll{color:#fff}
.site-footer .contact-line span{color:#f6b45a}
.site-footer .phone{color:#f6d087}
</style>
</head>
<body>

<header class="site-header abs">
  <div class="brand abs"><span class="brand-mark"></span><span class="brand-name">Brisko</span></div>
  <div class="lang abs">Select Language: <b>EN</b> | <em>RS</em></div>
  <div class="contact-line abs" style="left:560px;top:48px">Hours:&nbsp; <span>Mon - Fri: 10:00 - 19:00</span></div>
  <div class="contact-line abs" style="left:560px;top:69px">Email :&nbsp; <span style="font-weight:400">info@brisko.com</span></div>
  <div class="toll abs" style="left:752px;top:48px">Toll Free:</div>
  <div class="phone abs" style="left:752px;top:63px">1800 555 0147</div>
</header>

<div class="social abs"><span>Frendo</span><span>Chirpa</span><span>Pellix+</span></div>
<nav class="main-nav abs">
  <a class="current" href="#" style="left:517px">Home</a>
  <a href="#" style="left:597px">About</a>
  <a href="#" style="left:664px">Services</a>
  <a href="#" style="left:742px">Portfolio</a>
  <a href="#" style="left:823px">Contact Us</a>
</nav>

<section class="hero abs">
  <h1>Contextual<br><span class="dark">Advertising</span></h1>
  <p>Effective and quick way to increase sales. Quick Start and flexible adjustment of display ads can attract the attention of the target audience to the products and services of the company.</p>
  <div class="hero-arrows">
    <span><svg width="8" height="10"><path d="M6 1 2 5l4 4" fill="none" stroke="#444" stroke-width="2"/></svg></span>
    <span><svg width="8" height="10"><path d="M2 1l4 4-4 4" fill="none" stroke="#444" stroke-width="2"/></svg></span>
  </div>
  <div class="hero-screen" role="img" aria-label="Monitor showing a search results page with highlighted ads"></div>
  <svg class="hero-plus" width="34" height="34"><path d="M17 2v30M2 17h30" stroke="#1a1a1a" stroke-width="5"/></svg>
  <div class="hero-keywords" role="img" aria-label="Cascading lettering of the word optimization"></div>
  <div class="demo-btn">WATCH A DEMO</div>
</section>

<section class="card intro abs">
  <h2>Contextual Advertising</h2>
  <p>Contextual advertising will lead to your site targeted visitors with the regions selected phrases and a certain time. You can order advertising in three systems: Murelka, Tavrun, Pellix Bidwords.<br>Contextual advertising - one of the most successful ways to promote products and services. It allows the user not only gets a direct response to the request, but also the opportunity to go directly to the desired page of the site, the information you need to know to buy or order.<br>Just as in the promotion of this tool is different full coverage of narrowly targeted audiences. You get new customers in a short time and can quickly adjust the campaign with the latest requirements.</p>
  <span class="btn">READ MORE</span>
</section>

<section class="card how abs">
  <h2>How Does It Works</h2>
  <p>Aliquam molestie, mi et imperdiet euismod, dui purus auctor tellus, et interdum lacus lectus et ante. Sed accumsan sollicitudin sapien, sit amet adipiscing turpis gravida ac. In congue, neque ac lobortis volutpat, libero mauris varius mi, vitae suscipit ipsum ligula vitae risus.</p>
  <span class="btn">READ MORE</span>
  <div class="how-shot" role="img" aria-label="Browser window with a search results page and sponsored listings"></div>
</section>

<section class="card benefits abs">
  <h2>Benefits of PPC Advertising</h2>
  <ul>
    <li class="benefit"><span class="num">1</span><p>Lorem ipsum dolor sit amet, consect- etuer adipiscing elit, sed diam nonummy nibh euismod tincidunt ut laoreet dolore magna aliquam erat volutpat.</p></li>
    <li class="benefit"><span class="num">2</span><p>Lorem ipsum dolor sit amet, consect- etuer adipiscing elit, sed diam nonummy nibh euismod tincidunt ut laoreet dolore magna aliquam erat volutpat.</p></li>
    <li class="benefit"><span class="num">3</span><p>Lorem ipsum dolor sit amet, consect- etuer adipiscing elit, sed diam nonummy nibh euismod tincidunt ut laoreet dolore magna aliquam erat volutpat.</p></li>
  </ul>
</section>

<aside class="card quick abs">
  <h3>QUICK ORDER</h3>
  <div class="field">Name</div>
  <div class="field">Email Address</div>
  <div class="field">Contact No</div>
  <div class="field area">Type Message</div>
  <div class="submit">SUBMIT NOW</div>
</aside>

<aside class="side-panel certified abs">
  <h3>CERTIFIED<br>AGENCY</h3>
  <div class="badge" role="img" aria-label="Certification badge"></div>
  <p>Vivamus egestas risus in magna varius commodo. Sed semper viverra</p>
  <p class="wide">egestas. Etiam pretium porttitor lectus, vel ornare neque porta volutpat.</p>
</aside>

<aside class="side-panel clients abs">
  <h3>OUR CLIENTS</h3>
  <div class="client-grid">
    <div class="client"><i></i>Norvena</div>
    <div class="client yellow">Kuchelo</div>
    <div class="client">Stekloff</div>
    <div class="client yellow">Belvika</div>
  </div>
</aside>

<section class="mint reviews abs">
  <span class="quote-mark" style="left:8px;top:2px">“</span>
  <h2>Customer Reviews</h2>
  <p>Aliquam molestie, mi et imperdiet euismod, dui purus auctor tellus, et interdum lacus lectus et ante. Sed accumsan sollicitudin sapien, sit amet adipiscing turpis gravida ac. In congue, neque ac lobortis volutpat, libero mauris varius mi, vitae suscipit ipsum ligula vitae risus.</p>
  <div class="reviewer"><b>Dmitri Olvanov ,</b><br><span>marketing director TK "Loftera Hall"</span></div>
  <span class="quote-mark" style="right:6px;top:92px">”</span>
</section>

<section class="mint news abs">
  <h2>Latest News</h2>
  <div class="date">AUGUST 21, 2013</div>
  <p>Aliquam molestie, mi et imperdiet euismod, dui purus auctor tellus, et interdum lacus lectus et ante. Sed accumsan sollicitudin sapien, sit amet adipiscing turpis gravida ac. In congue, neque ac lobortis volutpat, libero mauris varius mi, vitae suscipit ipsum ligula vitae risus. Duis aliquam nibh a dui iaculis viverra id a velit....</p>
  <span class="more">READ MORE</span>
</section>

<footer class="site-footer abs">
  <div class="brand abs"><span class="brand-mark"></span><span class="brand-name">Brisko</span></div>
  <div class="copy abs">Copyright © 2013. AllRight Reserved</div>
  <div class="contact-line abs" style="left:560px;top:21px">Hours:&nbsp; <span>Mon - Fri: 10:00 - 19:00</span></div>
  <div class="contact-line abs" style="left:560px;top:42px">Email :&nbsp; <span style="font-weight:400">info@brisko.com</span></div>
  <div class="toll abs" style="left:752px;top:21px">Toll Free:</div>
  <div class="phone abs" style="left:752px;top:36px">1800 555 0147</div>
</footer>

</body>
</html>
```